Create intro for YouTube Channel on Motorcycle Travel and General Travel worldwide

Easily usable with Adobe Premier Pro for travel and motorcycle videos. Need to have an intro animated design and a standard end design clips for both Motorcycle Videos and General Travel Videos.

Requirements
Must have
• Animation on the intros and ending's
Nice to have
• For the general travel video a world with a plane circling for the motorcycle something similar.

```html
<!DOCTYPE html>
<html lang="en">
<head>
<meta charset="utf-8">
<title>Off To Roam Free – Travel Adventures Intro</title>
<link rel="stylesheet" href="https://fonts.googleapis.com/css2?family=Luckiest+Guy&display=swap">
<style>
  :root {
    --sky-core: #f3f9fa;
    --sky-mid: #a9dbe1;
    --sky-edge: #5e9bab;
    --brand-red: #e8392c;
    --ink-dark: #3a3a3a;
    --paper-white: #ffffff;
    --globe-ocean: #a8d6e8;
    --plane-body: #f4f4f4;
  }
  * { margin: 0; padding: 0; box-sizing: border-box; }
  html, body { width: 1200px; height: 675px; overflow: hidden; }
  body { font-family: "Luckiest Guy", "Arial Black", sans-serif; }

  .intro-canvas {
    position: relative;
    width: 1200px;
    height: 675px;
    overflow: hidden;
    background:
      radial-gradient(ellipse 640px 540px at 650px 410px,
        var(--sky-core) 0%, #d4ecef 25%, var(--sky-mid) 55%, #7eb8c4 80%, var(--sky-edge) 100%);
  }

  .channel-mark {
    position: absolute;
    left: 756px;
    top: 119px;
    transform: translate(-50%, -50%);
    display: flex;
    align-items: center;
    gap: 12px;
  }
  .channel-mark__dot {
    width: 40px;
    height: 40px;
    border-radius: 50%;
    background: var(--brand-red);
  }
  .channel-mark__name {
    font-family: "Luckiest Guy", "Arial Black", sans-serif;
    font-size: 38px;
    line-height: 1;
    color: var(--ink-dark);
    letter-spacing: 1px;
  }

  .globe-illustration {
    position: absolute;
    left: 128px;
    top: 240px;
    width: 182px;
    height: 182px;
    border-radius: 50%;
    background: radial-gradient(circle at 40% 35%, #eaf5f8 0%, var(--globe-ocean) 55%, #5a9cc4 100%);
    box-shadow: 0 6px 14px rgba(0, 0, 0, 0.15);
  }

  .plane-illustration {
    position: absolute;
    left: 141px;
    top: 178px;
    width: 109px;
    height: 36px;
    border-radius: 18px;
    background: linear-gradient(90deg, var(--plane-body) 0%, #e6e6e6 72%, #d9534a 100%);
  }

  .title-block {
    position: absolute;
    inset: 0;
    width: 1200px;
    height: 675px;
    margin: 0;
    font-weight: normal;
  }
  .title-block svg { display: block; }
  .title-block__text {
    font-family: "Luckiest Guy", "Arial Black", sans-serif;
    text-transform: uppercase;
    stroke: var(--paper-white);
    stroke-width: 10px;
    stroke-linejoin: round;
    paint-order: stroke fill;
    filter: drop-shadow(4px 6px 4px rgba(0, 0, 0, 0.3));
  }
  .title-block__headline { font-size: 62px; fill: var(--ink-dark); }
  .title-block__headline .accent { fill: var(--brand-red); }
  .title-block__tagline { font-size: 48px; fill: var(--brand-red); }
</style>
</head>
<body>
  <main class="intro-canvas">
    <div class="channel-mark">
      <span class="channel-mark__dot"></span>
      <span class="channel-mark__name">Roamwell</span>
    </div>

    <div class="plane-illustration" role="img" aria-label="Small white and red passenger jet circling the globe"></div>
    <div class="globe-illustration" role="img" aria-label="Illustrated Earth globe showing Australia and surrounding ocean"></div>

    <h1 class="title-block">
      <svg width="1200" height="675" viewBox="0 0 1200 675" aria-label="Off To Roam Free – Travel Adventures">
        <g transform="rotate(-5 472 318)">
          <text class="title-block__text title-block__headline" x="472" y="318" textLength="576" lengthAdjust="spacingAndGlyphs"><tspan class="accent">Off</tspan> To Roam <tspan class="accent">Free</tspan></text>
          <text class="title-block__text title-block__tagline" x="537" y="380" textLength="438" lengthAdjust="spacingAndGlyphs">Travel Adventures</text>
        </g>
      </svg>
    </h1>
  </main>
</body>
</html>
```